Business Card and Word .doc header and footer required

I need a business card designed for my cybersecurity consulting company. Also required, is a header and footer to be ued for my word documents.
Attached is the Logo design, font and rgb used.

Industry/Entity Type

Cyber Security Consulting

Contact Information for Business Card

Name, Phone, email, website

Colors
0054AA
0677BA
7BADD7
CADEEF
E8F1F8

Requirements
Must have
• Sleek, modern

```html
<!DOCTYPE html>
<html lang="en">
<head>
<meta charset="utf-8">
<title>Halvern Ridge Consulting – Business Card</title>
<link rel="stylesheet" href="https://fonts.googleapis.com/css2?family=Montserrat:wght@500;600;700&display=swap">
<style>
  :root {
    --backdrop: #eceded;
    --card-dark: #2c2d31;
    --card-light: #f7f8f8;
    --navy: #1d2b44;
    --blue-deep: #0054aa;
    --blue: #0677ba;
    --blue-soft: #7badd7;
    --text-dark: #2a2d33;
    --text-silver: #d9dbde;
  }
  * { margin: 0; padding: 0; box-sizing: border-box; }
  html, body {
    width: 1200px; height: 794px; overflow: hidden;
    background: var(--backdrop);
    font-family: "Montserrat", sans-serif;
  }
  .stage {
    position: relative; width: 1200px; height: 794px;
    display: flex; align-items: center; justify-content: center; gap: 60px;
  }
  .card {
    position: relative; width: 520px; height: 297px; overflow: hidden;
    box-shadow: 0 6px 18px rgba(0,0,0,0.18);
  }

  /* Front */
  .card-front { background: var(--card-dark); }
  .front-ring {
    position: absolute; right: -70px; top: -30px;
    width: 300px; height: 300px; border-radius: 50%;
    border: 26px solid var(--blue);
    background: transparent;
  }
  .front-wordmark {
    position: absolute; left: 42px; bottom: 46px;
    color: var(--text-silver); font-weight: 600;
    font-size: 22px; letter-spacing: 1.5px; line-height: 1.25;
    text-transform: uppercase;
  }

  /* Back */
  .card-back { background: var(--card-light); }
  .back-band {
    position: absolute; left: 0; right: 0; bottom: 0; height: 14px;
    background: var(--blue);
  }
  .brand {
    position: absolute; left: 48px; top: 112px;
    display: flex; align-items: center; gap: 14px;
  }
  .brand-dot {
    width: 40px; height: 40px; border-radius: 50%;
    background: var(--blue); flex: none;
  }
  .brand-name {
    color: var(--navy); font-weight: 700; font-size: 17px;
    letter-spacing: 1px; line-height: 1.25; text-transform: uppercase;
  }
  .contact-block { position: absolute; left: 300px; top: 58px; }
  .person-name {
    color: var(--blue); font-weight: 700; font-size: 20px; letter-spacing: 0.5px;
    text-transform: uppercase;
  }
  .person-title {
    color: var(--blue); font-weight: 500; font-size: 15px; margin: 4px 0 0 12px;
  }
  .contact-list { list-style: none; margin: 26px 0 0 24px; }
  .contact-list li {
    display: flex; align-items: center; gap: 10px;
    color: var(--text-dark); font-size: 12.5px; font-weight: 500; margin-bottom: 9px;
  }
  .contact-list svg { width: 14px; height: 14px; flex: none; }
</style>
</head>
<body>
<main class="stage">
  <section class="card card-front" aria-label="Business card front">
    <div class="front-ring" aria-hidden="true"></div>
    <p class="front-wordmark">Halvern Ridge<br>Consulting</p>
  </section>

  <section class="card card-back" aria-label="Business card back">
    <div class="brand">
      <span class="brand-dot" aria-hidden="true"></span>
      <p class="brand-name">Halvern Ridge<br>Consulting</p>
    </div>

    <div class="contact-block">
      <h1 class="person-name">Marco Ellis</h1>
      <p class="person-title">Owner</p>
      <ul class="contact-list">
        <li>
          <svg viewBox="0 0 14 14" fill="none" stroke="#0677ba" stroke-width="1.2"><rect x="4" y="1" width="6" height="12" rx="1"/><line x1="6.3" y1="11" x2="7.7" y2="11"/></svg>
          555.014.7720
        </li>
        <li>
          <svg viewBox="0 0 14 14" fill="none" stroke="#0677ba" stroke-width="1.2"><rect x="1" y="3" width="12" height="8"/><polyline points="1,3 7,8 13,3"/></svg>
          marco@halvernridge.com
        </li>
        <li>
          <svg viewBox="0 0 14 14" fill="none" stroke="#0677ba" stroke-width="1.1"><circle cx="7" cy="7" r="5.5"/><ellipse cx="7" cy="7" rx="2.4" ry="5.5"/><line x1="1.5" y1="7" x2="12.5" y2="7"/></svg>
          www.halvernridge.com
        </li>
      </ul>
    </div>

    <div class="back-band" aria-hidden="true"></div>
  </section>
</main>
</body>
</html>
```